Awesome photographers card for an awesome new business

Double sided business card Black background and silver logo in middle on one side. Details on otherside. please keep it simple

Industry/Entity Type

Photographer

Contact Information for Business Card

Colin Fairweather
0452816307
ColinFairweatherPhotography57@mailvane.com
www.ColinFairweatherPhotography.com.au
Instagram _Colin_fairweather

Requirements
Must have
• My logo in Silver
• please use instagram logo instead of "Instagram"

```html
<!DOCTYPE html>
<html lang="en">
<head>
<meta charset="utf-8">
<title>Colin Fairweather Photography – Business Card</title>
<link href="https://fonts.googleapis.com/css2?family=Lato:wght@300;400;700&display=swap" rel="stylesheet">
<style>
  :root {
    --backdrop: #2b2b2c;
    --card-dark: #15181b;
    --card-mid: #2a2f34;
    --silver: #d9dcdf;
    --silver-dim: #aab0b5;
    --ink-white: #f4f5f6;
    --icon-ink: #1b1e21;
  }
  * { box-sizing: border-box; margin: 0; padding: 0; }
  html, body {
    width: 1200px; height: 791px; overflow: hidden;
    background: var(--backdrop);
    font-family: "Lato", Arial, sans-serif;
  }
  .stage {
    width: 1200px; height: 791px;
    display: flex; align-items: center; justify-content: center; gap: 36px;
  }
  .card {
    width: 560px; height: 320px;
    background: radial-gradient(ellipse at 50% 40%, var(--card-mid) 0%, var(--card-dark) 75%);
    box-shadow: 0 14px 30px rgba(0,0,0,.55);
    position: relative;
    color: var(--ink-white);
  }
  /* Front */
  .card-front { display: flex; align-items: center; justify-content: center; gap: 14px; }
  .brand-dot {
    width: 22px; height: 22px; border-radius: 50%;
    border: 2px solid var(--silver);
  }
  .brand-name {
    font-weight: 400; font-size: 30px; letter-spacing: 3px;
    color: var(--silver); text-transform: uppercase;
  }
  /* Back */
  .card-back {
    display: flex; flex-direction: column; align-items: center; justify-content: center;
    text-align: center;
  }
  .person-name { font-size: 24px; font-weight: 300; letter-spacing: 1px; text-transform: uppercase; }
  .person-name strong { font-weight: 700; }
  .person-role { font-size: 11px; font-weight: 700; letter-spacing: 2.5px; margin-top: 2px; margin-bottom: 12px; }
  .contact { display: flex; flex-direction: column; align-items: center; margin-bottom: 7px; }
  .contact-icon {
    width: 18px; height: 18px; border-radius: 4px; background: var(--ink-white);
    display: flex; align-items: center; justify-content: center; margin-bottom: 4px;
  }
  .contact-text { font-size: 13px; font-weight: 400; letter-spacing: .4px; }
  .contact-text.phone { letter-spacing: 3px; }
  .rule { width: 310px; border-top: 2px dotted var(--silver-dim); margin: 2px 0 9px; }
  .social-square { width: 9px; height: 9px; border: 1.6px solid var(--icon-ink); border-radius: 2px; }
</style>
</head>
<body>
<main class="stage">
  <section class="card card-front" aria-label="Card front">
    <span class="brand-dot"></span>
    <span class="brand-name">Colin Fairweather</span>
  </section>

  <section class="card card-back" aria-label="Card back">
    <h1 class="person-name"><strong>Colin</strong> Fairweather</h1>
    <p class="person-role">PHOTOGRAPHER</p>

    <div class="contact">
      <span class="contact-icon">
        <svg width="12" height="12" viewBox="0 0 24 24"><path fill="var(--icon-ink)" d="M6.6 10.8a15.1 15.1 0 0 0 6.6 6.6l2.2-2.2c.3-.3.7-.4 1-.2 1.1.4 2.3.6 3.6.6.6 0 1 .4 1 1V20c0 .6-.4 1-1 1C10.6 21 3 13.4 3 4c0-.6.4-1 1-1h3.5c.6 0 1 .4 1 1 0 1.3.2 2.5.6 3.6.1.3 0 .7-.2 1z"/></svg>
      </span>
      <span class="contact-text phone">0452816307</span>
    </div>

    <div class="contact">
      <span class="contact-icon">
        <svg width="12" height="12" viewBox="0 0 24 24" fill="none" stroke="var(--icon-ink)" stroke-width="2"><circle cx="12" cy="12" r="9"/><ellipse cx="12" cy="12" rx="4" ry="9"/><path d="M3 12h18M5 7h14M5 17h14"/></svg>
      </span>
      <span class="contact-text">www.ColinFairweatherPhotography.com.au</span>
    </div>

    <div class="rule"></div>

    <div class="contact">
      <span class="contact-icon">
        <svg width="12" height="12" viewBox="0 0 24 24" fill="none" stroke="var(--icon-ink)" stroke-width="2.4"><circle cx="12" cy="12" r="4"/><path d="M16 8v5.5a2.5 2.5 0 0 0 5 0V12a9 9 0 1 0-3.5 7.1"/></svg>
      </span>
      <span class="contact-text">ColinFairweatherPhotography57@mailvane.com</span>
    </div>

    <div class="rule"></div>

    <div class="contact">
      <span class="contact-icon"><span class="social-square"></span></span>
      <span class="contact-text">_Colin_fairweather</span>
    </div>
  </section>
</main>
</body>
</html>
```